Business Cards for a company that provides webstore services to veterinarians

We need business cards designed for our main service PawCartHub. PawCartHub is a webstore that veterinarian clinics can use to that will allow their clients to purchase products for their pets. Our company is Brindlow Veterinary Solutions (BVS). Our mission statement is We love pets! We will do everything possible to facilitate along, healthy and happy relationship with their families.

Target Market(s)

Veterinarians

Industry/Entity Type

Veterinary

Contact Information for Business Card

I would like the design to incorporate the colours our our company. Cards should have room for employee name, title (only necessary in two instances), phone number, mobile number, email address and linkedin symbol and related profile name ie Marla Quinton. I would like the PawCartHub logo to appear on one side and BVS logo to appear on the other. I will need both an english and french version. I can provide the french translation. Please focus on english version and then we will translate

Colors

Designer to choose colors to be used in the design.

Requirements
Must have
• one side - PawCartHub logo with persons name, phone number, mobile number, email address
• second side - BVS logo
• colours should be consistent with our company. colours are as follows:
• Red
• RGB: 190 / 30 / 45
• CYMK: 14 / 100 / 90 /10
• Hex: #BE1E2D
• Gray
• RGB: 88 / 89 / 86
• CYMK: 3 / 2 / 0 /64
• Hex: #585956
Nice to have
• address of company - can be on either side address is 4817 Feldmoor Street Suite 305 Burlington ON K2R 6T4. Toll free number will vary depending on person
• Linkedin symbol and name of person
• on second side with BVS logo our company's mission statement
Should not have
• nothing comes to mind

```html
<!DOCTYPE html>
<html lang="en">
<head>
<meta charset="utf-8">
<title>PawCartHub / Brindlow Veterinary Solutions Business Card</title>
<link rel="stylesheet" href="https://fonts.googleapis.com/css2?family=Lato:ital,wght@0,400;0,700;0,900;1,400&display=swap">
<style>
  :root {
    --brand-red: #BE1E2D;
    --brand-red-dark: #A8192A;
    --brand-red-light: #D0283A;
    --brand-gray: #585956;
    --card-white: #F7F7F7;
    --stage: #EEEEEE;
    --ink-white: #FFFFFF;
  }
  * { margin: 0; padding: 0; box-sizing: border-box; }
  html, body { width: 1200px; height: 586px; overflow: hidden; }
  body {
    background: var(--stage);
    font-family: "Lato", Arial, sans-serif;
    position: relative;
  }
  .card {
    position: absolute;
    top: 143px;
    width: 500px;
    height: 300px;
    overflow: hidden;
  }

  /* Front: PawCartHub */
  .card-front { left: 72px; }
  .front-texture {
    position: absolute; inset: 0;
    background: linear-gradient(135deg, var(--brand-red-light) 0%, var(--brand-red) 35%, var(--brand-red-dark) 60%, var(--brand-red) 85%, var(--brand-red-light) 100%);
  }
  .front-wordmark {
    position: absolute; left: 0; right: 0; top: 112px;
    text-align: center;
    color: var(--ink-white);
    font-weight: 400;
    font-size: 48px;
    line-height: 56px;
  }
  .front-profile {
    position: absolute; left: 0; right: 0; top: 259px;
    display: flex; justify-content: center; align-items: center; gap: 5px;
    color: var(--ink-white);
    font-weight: 700;
    font-size: 12.5px;
  }
  .profile-square { width: 13px; height: 13px; background: var(--ink-white); border-radius: 1px; }

  /* Back: Brindlow Veterinary Solutions */
  .card-back { left: 628px; background: var(--card-white); }
  .back-bands { position: absolute; inset: 0; }
  .back-paws {
    position: absolute; right: 0; top: 0; width: 80px; height: 300px;
    background: linear-gradient(180deg, rgba(255,255,255,0.05), rgba(255,255,255,0.02));
  }
  .back-brand {
    position: absolute; left: 0; width: 246px; top: 120px;
    display: flex; flex-direction: column; align-items: center; gap: 10px;
  }
  .back-brand-dot {
    width: 14px; height: 14px; border-radius: 50%;
    background: var(--brand-red);
  }
  .back-brand-name {
    color: var(--brand-red);
    font-weight: 700;
    font-size: 18px;
    line-height: 22px;
    text-align: center;
  }
  .back-mission {
    position: absolute; left: 0; width: 246px; top: 253px;
    text-align: center;
    color: var(--brand-red);
    font-weight: 700;
    font-size: 11px;
    letter-spacing: 6.5px;
  }
  .contact {
    position: absolute; left: 305px; top: 52px;
    color: var(--ink-white);
  }
  .contact-name { font-weight: 900; font-size: 17px; }
  .contact-title { font-style: italic; font-size: 11px; margin-top: 1px; }
  .contact-address { margin-top: 38px; font-weight: 700; font-size: 12px; line-height: 20px; }
  .contact-lines { margin-top: 34px; list-style: none; font-size: 12px; }
  .contact-lines li { display: flex; align-items: center; height: 22px; }
  .contact-icon { width: 12px; height: 12px; margin-right: 12px; margin-left: 2px; }
</style>
</head>
<body>

<section class="card card-front">
  <div class="front-texture" role="img" aria-label="Red low-poly faceted background texture"></div>
  <div class="front-wordmark">PawCartHub</div>
  <div class="front-profile"><span class="profile-square"></span>/pawcarthub.ca</div>
</section>

<section class="card card-back">
  <svg class="back-bands" width="500" height="300" viewBox="0 0 500 300">
    <polygon points="228,0 500,0 500,300 288,300" fill="var(--brand-red)"/>
    <polygon points="204,0 212,0 271,300 263,300" fill="var(--brand-red)"/>
    <polygon points="217,0 222,0 281,300 276,300" fill="var(--brand-red)"/>
  </svg>
  <div class="back-paws" role="img" aria-label="Faint trail of paw prints"></div>

  <div class="back-brand">
    <span class="back-brand-dot"></span>
    <div class="back-brand-name">Brindlow<br>Veterinary Solutions</div>
  </div>
  <div class="back-mission">WE LOVE PETS</div>

  <div class="contact">
    <div class="contact-name">Marla Quinton</div>
    <div class="contact-title">Owner &amp; Founder</div>
    <div class="contact-address">4817 Feldmoor Street Suite,<br>305 Burlington ON K2R 6T4</div>
    <ul class="contact-lines">
      <li>
        <svg class="contact-icon" viewBox="0 0 12 12"><path d="M1 4 Q6 0 11 4 L9 5.5 L8 4 H4 L3 5.5 Z M3 6 H9 L10 10 H2 Z" fill="#fff"/></svg>
        +1 905 555 0142
      </li>
      <li>
        <svg class="contact-icon" viewBox="0 0 12 12"><rect x="3.5" y="0.5" width="5" height="11" rx="1" fill="none" stroke="#fff"/><rect x="5" y="9" width="2" height="1" fill="#fff"/></svg>
        +1 905 555 0187
      </li>
      <li>
        <svg class="contact-icon" viewBox="0 0 12 12"><rect x="0.5" y="2.5" width="11" height="7.5" fill="#fff"/><path d="M0.5 2.5 L6 7 L11.5 2.5" fill="none" stroke="var(--brand-red)"/></svg>
        marla.quinton@mailbox.ca
      </li>
    </ul>
  </div>
</section>

</body>
</html>
```